Web Design job: SaaS start-up needs a cutting-edge web design

What's Needed:
- All designs files created
- Fully coded implementation in HTML/CSS/Bootstrap
- Pages: 5 -- see content here http://www.TeamVellora.com
-- Home Page
-- The Hidden Value
-- Benefits
-- About us
-- Careers
- The existing site has the textual content for each page. We can tweak to meet specific designs if needed.
- You will need to update/create image and interactive content for pages.

Reference:
Our existing website has a lot of content on it for reference -
http://www.TeamVellora.com

Description:
We need a web design that focuses in the UX and conveys the idea of magically fixing company problems by way of using our software.

Home Page
The main goal is to Drive Sales of the SaaS tool. When a visitor lands on our home page they should see: What we do, How we can help their problem and How to contact us.
1. Quickly understand What We Do
-- we sell SaaS software.
-- Need to quickly convey what our software does. It's seems complicated but really its not. See the description in about us for more info and visit our existing site.

2. How we can help their problem
-- We aim to solve any problem related to employees
-- Even if the visitor does not have a specific problem in mind, there are several areas organizations can always improve: (some examples below)
---- Create Stronger, More Productive Teams
---- Build Better Communications Pathways
---- Encourage Innovation and Positive Change
---- Develop and Retain Strong "Company Culture"

3. Be able to Contact Us to get started
-- contacting us to get a sales lead is the ultimate goal.
-- the user should not have to hunt to contact us. needs to be easy.

Other Pages (Hidden Value, Benefit, About Us, Careers):
-- These are informative pages about our software and process.
-- If we grab the attention of the user on the home page then these are the pages that they will explore for more info.
-- Should be able to link to these pages from the main nav or from sections with the homepage. For example: What We Do sections could link to the benefits page. How we help their problem sections could link to the Hidden Value page. Regardless of what links to where, the idea is that we will be able to nav to other areas.

About Us:
Our company name is TeamVellora (as in Organizational Analysis). We provide a software as a service (SaaS) that uses a simple 6-question survey to analyze the relationships of people within an Organization and provide leaders with ground-breaking Insights about their teams, interactive social network data visualizations to explore their team's composition and we give detailed profiles of the key players (i.e, who are the Social Bridges, Who are the Knowledge Bottlenecks, Who are the Best Mentors, Who are the people that are completely disconnected/out of the loop). Leaders then use this information to make high level organizational decisions.

What's unique about our software:
-- Powerful analysis results from just a 6-question "pulse-surveys"
-- Innovative Tools for visually exploring the organization through relationships as opposed to org-chart
-- Get real-time results as opposed to waiting months with traditional methods
-- Traditional Org-charts represent the organization's skeleton, whereas we uncover the organization's neural network (how it solves problems).

Preferred fonts (but could be convinced otherwise if looks great):
-- Section titles - Aleo
-- Main body - Lato
-- TeamVellora logo - Philosopher

Things we like:
-- We like a big slider as the top of the landing page.

Colors to include:
-- Colors in the logo (red, blue, green, teal) as accent colors

Feel of the site:
-- Cutting-edge Software
-- Professional
-- Social Network flare (we analyze relationships)

Note:
If we find a great match with a designer there is strong possibility to continue the relationship with follow on work redesigning our web-based application.

Target Market(s)

Current customers are Corwin Pale & Hargrove, Upland Mutual Bank.
We target anyone that manages a large team. Such as Corporate Leaders, High Level Managers, HR Leaders

Industry/Entity Type

Business Software

Contact Information for Business Card

Logo image
Name of company "TEAMVELLORA" In Philosopher font.
Tagline: "Unlock the Hidden Value In Your Teams"
Person's Name, Title, email, phone.

Coding

Coded - Design and coding required

Number of Pages Required

4 page

Font styles to use
Other font styles liked:
• Lato, Philosopher, Aero

Colors
ec1f27
0255a3

Requirements
Must have
• See description.
Nice to have
• Things we like:
• We like a big slider as the top of the landing page. Ours is a little clunky and outdated but something fresh and sleek would be great.
• Colors to include:
• We would like to use the colors in the logo as accent colors in the site to give a consistent look and feel.
• Feel of the site:
• Cutting-edge Software
• Professional
• Social Network flare (we analyze relationships)

```html
<!DOCTYPE html>
<html lang="en">
<head>
<meta charset="utf-8">
<title>TeamVellora — Organizational Analysis</title>
<link href="https://fonts.googleapis.com/css2?family=Roboto+Slab:wght@300;400;700&display=swap" rel="stylesheet">
<style>
  :root {
    --brand-blue: #0255a3;
    --brand-red: #ec1f27;
    --ink: #333333;
    --ink-soft: #666666;
    --line: #d6d6d6;
    --band: #f4f4f4;
    --white: #ffffff;
    --footer: #1f1f1f;
  }
  * { box-sizing: border-box; margin: 0; padding: 0; }
  html, body { width: 1200px; height: 2667px; overflow: hidden; }
  body {
    position: relative;
    background: var(--white);
    color: var(--ink);
    font-family: "Roboto Slab", Rockwell, Georgia, serif;
    font-weight: 300;
  }

  /* Header */
  .site-header { position: absolute; left: 0; top: 0; width: 1200px; height: 119px; border-top: 3px solid #e2e2e2; background: var(--white); }
  .brand { position: absolute; left: 98px; top: 58px; display: flex; align-items: center; gap: 10px; }
  .brand-dot { width: 18px; height: 18px; border-radius: 50%; background: var(--brand-blue); }
  .brand-name { font-size: 24px; font-weight: 700; color: var(--brand-blue); letter-spacing: 0.5px; }
  .topbar { position: absolute; right: 98px; top: 20px; font-size: 12px; color: var(--ink-soft); display: flex; gap: 10px; align-items: center; }
  .topbar svg { vertical-align: -2px; margin-right: 5px; }
  .main-nav { position: absolute; right: 98px; top: 73px; display: flex; gap: 50px; font-size: 13px; font-weight: 400; color: var(--ink); }
  .main-nav .is-active { color: var(--brand-blue); }

  /* Hero */
  .hero { position: absolute; left: 0; top: 119px; width: 1200px; height: 583px;
    background:
      radial-gradient(circle at 70% 30%, rgba(255,255,255,0.55), transparent 35%),
      radial-gradient(circle at 20% 70%, rgba(120,170,220,0.5), transparent 45%),
      linear-gradient(135deg, #1e4f86 0%, #6d98c4 45%, #b9cfe4 65%, #3c6c9e 100%); }
  .hero-title { position: absolute; left: 0; width: 1200px; top: 448px; text-align: center; font-size: 34px; font-weight: 700; color: var(--white); letter-spacing: 1px; text-shadow: 0 2px 6px rgba(0,0,0,0.45); }
  .hero-dots { position: absolute; top: 543px; left: 0; width: 1200px; display: flex; justify-content: center; gap: 14px; }
  .hero-dots span { width: 11px; height: 11px; border-radius: 50%; background: #2a4f7a; border: 2px solid #d8e5f2; }
  .hero-dots .is-current { background: var(--white); }

  /* Section titles */
  .section-title { position: absolute; left: 0; width: 1200px; text-align: center; font-size: 27px; font-weight: 400; color: var(--ink); }

  /* What we do */
  .intro { position: absolute; left: 178px; top: 812px; width: 844px; text-align: center; font-size: 12.5px; line-height: 21px; color: var(--ink-soft); }
  .feature { position: absolute; top: 920px; width: 240px; text-align: center; }
  .feature-icon { width: 102px; height: 102px; margin: 0 auto; border: 1px solid var(--line); border-radius: 50%; display: flex; align-items: center; justify-content: center; }
  .feature-label { margin-top: 28px; font-size: 17px; line-height: 26px; color: var(--ink); }

  /* About */
  .about { position: absolute; left: 0; top: 1148px; width: 1200px; height: 438px; background: var(--band); }
  .about-title { position: absolute; left: 98px; top: 52px; font-size: 25px; font-weight: 400; }
  .about-text { position: absolute; left: 98px; top: 115px; width: 494px; font-size: 12.3px; line-height: 20.6px; color: var(--ink-soft); text-align: justify; }
  .btn { position: absolute; background: var(--brand-blue); color: var(--white); font-size: 12px; font-weight: 400; display: flex; align-items: center; justify-content: center; }
  .btn-learn { left: 98px; top: 319px; width: 126px; height: 51px; }
  .network-art { position: absolute; left: 711px; top: 61px; width: 311px; height: 311px; border-radius: 50%;
    background: radial-gradient(circle at 45% 45%, rgba(200,40,90,0.35), rgba(120,70,200,0.28) 35%, rgba(40,90,220,0.18) 55%, rgba(244,244,244,0) 72%); }

  /* Help */
  .phone { position: absolute; top: 1735px; width: 149px; height: 269px; border: 1.5px solid #cfcfcf; border-radius: 18px; background: var(--white); }
  .phone-speaker { position: absolute; left: 59px; top: 20px; width: 31px; height: 5px; border: 1.5px solid #cfcfcf; border-radius: 3px; }
  .phone-screen { position: absolute; left: 12px; top: 43px; width: 123px; height: 179px; border: 1.5px solid #cfcfcf; display: flex; align-items: center; justify-content: center; }
  .phone-button { position: absolute; left: 62px; top: 231px; width: 24px; height: 24px; border: 1.5px solid #cfcfcf; border-radius: 50%; }
  .flow-arrow { position: absolute; top: 1840px; }
  .help-label { position: absolute; top: 2030px; width: 300px; text-align: center; font-size: 17px; line-height: 27px; color: var(--ink); }

  /* Contact */
  .contact { position: absolute; left: 0; top: 2151px; width: 1200px; height: 441px;
    background: linear-gradient(160deg, #f6f6f4 0%, #eeeeec 50%, #f4f4f2 100%); }
  .contact-heading { position: absolute; font-size: 19px; font-weight: 300; color: var(--ink); line-height: 24px; }
  .field { position: absolute; left: 98px; width: 467px; background: var(--white); border: 1px solid #d9d9d9; border-radius: 2px; font-size: 10px; color: #888; padding: 12px 10px; }
  .btn-send { left: 457px; top: 322px; width: 108px; height: 41px; }
  .contact-info { position: absolute; left: 736px; top: 100px; font-size: 12.5px; line-height: 22px; color: var(--ink); font-weight: 400; }
  .contact-info .gap { display: block; height: 22px; }
  .social { position: absolute; top: 342px; left: 738px; display: flex; gap: 17px; }
  .social-link { width: 42px; height: 42px; border-radius: 50%; background: var(--white); box-shadow: 0 1px 3px rgba(0,0,0,0.15); display: flex; align-items: center; justify-content: center; }
  .social-link::after { content: ""; width: 10px; height: 10px; border-radius: 50%; background: var(--brand-blue); }

  /* Footer */
  .site-footer { position: absolute; left: 0; top: 2592px; width: 1200px; height: 75px; background: var(--footer); color: #dddddd; font-size: 11.5px; font-weight: 400; display: flex; align-items: center; justify-content: center; }
</style>
</head>
<body>

<header class="site-header">
  <div class="brand"><span class="brand-dot"></span><span class="brand-name">TEAMVELLORA</span></div>
  <div class="topbar">
    <span><svg width="12" height="12" viewBox="0 0 12 12"><rect x="1" y="1" width="10" height="10" rx="2" fill="#777"/><path d="M4 3.5c0 2.5 2 4.5 4.5 4.5l.5-1.2-1.3-.6-.6.6c-.9-.4-1.5-1-1.9-1.9l.6-.6-.6-1.3z" fill="#fff"/></svg>Phone : (555) 418 2290</span>
    <span>|</span>
    <span><svg width="12" height="12" viewBox="0 0 12 12"><circle cx="6" cy="6" r="5.5" fill="#777"/><path d="M.5 6h11M6 .5c-3 3-3 8 0 11M6 .5c3 3 3 8 0 11" stroke="#fff" stroke-width=".8" fill="none"/></svg>language : English ▾</span>
  </div>
  <nav class="main-nav">
    <span class="is-active">⌂ HOME</span><span>ABOUT US</span><span>WHAT WE DO</span><span>SERVICES</span><span>CONTACT US</span>
  </nav>
</header>

<section class="hero" role="img" aria-label="Photo of a hand on a laptop keyboard overlaid with glowing data network lines">
  <h1 class="hero-title">ORGANIZATIONAL ANALYSIS</h1>
  <div class="hero-dots"><span></span><span class="is-current"></span><span></span><span></span></div>
</section>

<h2 class="section-title" style="top:760px">What We Do</h2>
<p class="intro">Our company name is TeamVellora (as in Organizational Analysis). We provide a software as a service (SaaS) that uses a simple 6-question survey to analyze the relationships of people within an Organization and provide leaders with ground-breaking Insights about their teams, interactive social network data visualizations to explore their team's composition</p>

<div class="feature" style="left:65px">
  <div class="feature-icon"><svg width="46" height="46" viewBox="0 0 46 46" fill="none" stroke="#ec1f27" stroke-width="1.6"><circle cx="23" cy="23" r="3"/><path d="M16 16a10 10 0 0 0 0 14M30 16a10 10 0 0 1 0 14M11 11a17 17 0 0 0 0 24M35 11a17 17 0 0 1 0 24"/></svg></div>
  <div class="feature-label">On-Line Pulse Surver</div>
</div>
<div class="feature" style="left:344px">
  <div class="feature-icon"><svg width="46" height="46" viewBox="0 0 46 46" fill="none" stroke="#ec1f27" stroke-width="1.6"><rect x="13" y="10" width="20" height="26" rx="2"/><path d="M18 17h10M18 22h10M18 27h6M9 20h8M9 26h8"/></svg></div>
  <div class="feature-label">Proprietary Algorithms</div>
</div>
<div class="feature" style="left:625px">
  <div class="feature-icon"><svg width="46" height="46" viewBox="0 0 46 46" fill="none" stroke="#ec1f27" stroke-width="1.6"><path d="M23 8a10 10 0 0 0-6 18v4h12v-4a10 10 0 0 0-6-18z"/><path d="M18 34h10M20 38h6"/></svg></div>
  <div class="feature-label">Organizational Key<br>Insights</div>
</div>
<div class="feature" style="left:906px">
  <div class="feature-icon"><svg width="46" height="46" viewBox="0 0 46 46" fill="none" stroke="#ec1f27" stroke-width="1.6"><path d="M23 8l4.5 9.5 10.5 1.3-7.7 7.2 2 10.4L23 31.3l-9.3 5.1 2-10.4L8 18.8l10.5-1.3z"/></svg></div>
  <div class="feature-label">Expert Review and<br>Action Plans</div>
</div>

<section class="about">
  <h2 class="about-title">About Us</h2>
  <p class="about-text">Our company name is TeamVellora (as in Organizational Analysis). We provide a software as a service (SaaS) that uses a simple 6-question survey to analyze the relationships of people within an Organization and provide leaders with ground-breaking Insights about their teams, interactive social network data visualizations to explore their team's composition and we give detailed profiles of the key players (i.e, who are the Social Bridges, Who are the Knowledge Bottlenecks, Who are the Best Mentors, Who are the people that are completely disconnected/out of the loop). Leaders then use this information to make high level organizational decisions.</p>
  <div class="btn btn-learn">LEARN MORE</div>
  <div class="network-art" role="img" aria-label="Colourful social network graph of connected nodes in red, purple, blue, green and orange"></div>
</section>

<h2 class="section-title" style="top:1641px">How we Can Help Their Problem</h2>

<div class="phone" style="left:219px">
  <div class="phone-speaker"></div>
  <div class="phone-screen"><svg width="70" height="50" viewBox="0 0 70 50" fill="none" stroke="#c4c4c4" stroke-width="1.6"><path d="M4 18l12-8 10 4 8-3 10 3 10-4 12 8M14 12l-6 16M56 12l6 16M20 30l8 8 4-2 4 4 4-2 4 2 6-6M26 22l10 6 8-4"/></svg></div>
  <div class="phone-button"></div>
</div>
<svg class="flow-arrow" style="left:393px" width="92" height="40" viewBox="0 0 92 40"><path d="M2 30 Q45 42 78 14" stroke="#cfcfcf" stroke-width="6" fill="none"/><path d="M70 6l18 2-8 16z" fill="#cfcfcf"/></svg>
<div class="phone" style="left:526px">
  <div class="phone-speaker"></div>
  <div class="phone-screen"><svg width="60" height="50" viewBox="0 0 60 50" fill="none" stroke="#c4c4c4" stroke-width="1.6"><path d="M8 18h10l18-10v32L18 30H8z"/><path d="M12 30l4 12h6l-3-12M44 16l8-4M44 24h10M44 32l8 4"/></svg></div>
  <div class="phone-button"></div>
</div>
<svg class="flow-arrow" style="left:710px" width="92" height="40" viewBox="0 0 92 40"><path d="M2 14 Q45 0 78 26" stroke="#cfcfcf" stroke-width="6" fill="none"/><path d="M68 34l20 2-6-18z" fill="#cfcfcf"/></svg>
<div class="phone" style="left:832px">
  <div class="phone-speaker"></div>
  <div class="phone-screen"><svg width="64" height="54" viewBox="0 0 64 54" fill="none" stroke="#c4c4c4" stroke-width="1.6"><rect x="4" y="12" width="44" height="30" rx="2"/><path d="M20 42v6h12v-6M14 48h24"/><circle cx="46" cy="14" r="7"/><circle cx="46" cy="14" r="12" stroke-dasharray="4 3"/></svg></div>
  <div class="phone-button"></div>
</div>

<div class="help-label" style="left:143px">We aim to solve any problem<br>related to employees</div>
<div class="help-label" style="left:451px">Create Stronger, More<br>Productive Teams</div>
<div class="help-label" style="left:756px">Build Better Communications<br>Pathways</div>

<section class="contact" aria-label="Contact section over a faint street map background">
  <h3 class="contact-heading" style="left:98px;top:60px">Contact Form:</h3>
  <div class="field" style="top:110px;height:40px">Name:</div>
  <div class="field" style="top:160px;height:40px">Email:</div>
  <div class="field" style="top:210px;height:98px">Message:</div>
  <div class="btn btn-send">SEND</div>

  <h3 class="contact-heading" style="left:736px;top:60px">Contact Info:</h3>
  <div class="contact-info">
    820 Larkfield Avenue<br>Suite 310<br>Brookhaven, VA 22190
    <span class="gap"></span>
    E-mail: info@teamvellora.com<br>Phone: 555 014 3362<br>Fax: &nbsp;&nbsp;&nbsp;&nbsp;555 014 3362
  </div>
  <h3 class="contact-heading" style="left:736px;top:300px">Social Media:</h3>
  <div class="social">
    <span class="social-link" aria-label="Social link 1"></span>
    <span class="social-link" aria-label="Social link 2"></span>
    <span class="social-link" aria-label="Social link 3"></span>
    <span class="social-link" aria-label="Social link 4"></span>
  </div>
</section>

<footer class="site-footer">teamvellora.com. © 2016 &nbsp;Privacy Policy</footer>

</body>
</html>
```